new letterhead/envelope/business card design for law firm

please see attached pdf of current letterhead, envelope and business card. I am also attaching my new logo that I would like to be used. basically, I am looking to refresh and simplify my letterhead/stationary and business card, keeping the following in mind:

overall, I am going for the following look:

-simple,
-modern,
-classy,
-professional

Target Market(s)

law firm clients

Industry/Entity Type

Law Firm

Contact Information for Business Card

see attachment

Font styles to use
Sans Serif

Requirements
Must have
• overall, I am going for the following look:
• -simple,
• -modern,
• -classy,
• -professional
Nice to have
• same as above
Should not have
• no serif fonts

```html
<!DOCTYPE html>
<html lang="en">
<head>
<meta charset="utf-8">
<title>Hartwell Law Stationery</title>
<link href="https://fonts.googleapis.com/css2?family=Roboto:wght@400;500;700&display=swap" rel="stylesheet">
<style>
  :root {
    --navy: #12284f;
    --green: #1f6b3a;
    --grey-text: #6b6f76;
    --backdrop: #efefef;
    --paper: #ffffff;
    --shadow: 0 2px 4px rgba(0,0,0,0.28);
  }
  * { margin: 0; padding: 0; box-sizing: border-box; }
  html, body { width: 1200px; height: 1197px; overflow: hidden; }
  body {
    background: var(--backdrop);
    font-family: "Roboto", Arial, sans-serif;
    color: var(--grey-text);
    position: relative;
  }
  .sheet { position: absolute; background: var(--paper); box-shadow: var(--shadow); }

  /* Brand lockup */
  .brand { position: absolute; display: flex; flex-direction: column; align-items: center; transform: translateX(-50%); }
  .brand-circle { border-radius: 50%; background: var(--navy); }
  .brand-name {
    font-family: "Roboto", Arial, sans-serif;
    font-weight: 700; color: var(--navy);
    letter-spacing: 0.06em; white-space: nowrap; text-align: center; line-height: 1.1;
  }

  /* Letterhead */
  .letterhead { left: 106px; top: 282px; width: 471px; height: 626px; }
  .letterhead .brand { left: 235px; top: 40px; }
  .letterhead .brand-circle { width: 38px; height: 38px; }
  .letterhead .brand-name { font-size: 16px; margin-top: 5px; }
  .letterhead-footer { position: absolute; left: 42px; right: 42px; top: 572px; font-size: 6.3px; line-height: 8.6px; }
  .footer-col { position: absolute; top: 0; }
  .footer-col.attorney { left: 0; }
  .footer-col.office { left: 110px; }
  .footer-web { position: absolute; right: 0; top: 26px; }
  .footer-web strong, .attorney-name { color: var(--navy); font-weight: 700; }
  .label { color: var(--navy); font-weight: 700; }

  /* Business card */
  .business-card { left: 617px; top: 282px; width: 270px; height: 155px; }
  .card-band { position: absolute; left: 0; right: 0; height: 6px; background: var(--navy); }
  .card-band.top { top: 0; }
  .card-band.bottom { bottom: 0; }
  .business-card .brand { left: 78px; top: 42px; }
  .business-card .brand-circle { width: 40px; height: 40px; }
  .business-card .brand-name { font-size: 17px; margin-top: 5px; }
  .card-details { position: absolute; right: 22px; text-align: right; font-size: 6.3px; line-height: 8.6px; }
  .card-details.identity { top: 25px; }
  .card-details.contact { top: 80px; }
  .card-details.address { top: 121px; }
  .card-name { color: var(--navy); font-weight: 700; font-size: 8.6px; line-height: 11px; }

  /* Envelope back */
  .envelope-back { left: 617px; top: 455px; width: 487px; height: 214px; overflow: hidden; }
  .envelope-flap { position: absolute; left: 0; top: 0; }

  /* Envelope front */
  .envelope-front { left: 617px; top: 695px; width: 488px; height: 214px; }
  .envelope-front .brand { left: 72px; top: 19px; }
  .envelope-front .brand-circle { width: 35px; height: 35px; }
  .envelope-front .brand-name { font-size: 15px; margin-top: 4px; }
  .return-address {
    position: absolute; left: 72px; top: 87px; transform: translateX(-50%);
    text-align: center; font-size: 6.3px; line-height: 8.2px; color: var(--navy); font-weight: 500; white-space: nowrap;
  }
</style>
</head>
<body>

  <section class="sheet letterhead" aria-label="Letterhead">
    <div class="brand">
      <div class="brand-circle"></div>
      <div class="brand-name">HARTWELL LAW</div>
    </div>
    <footer class="letterhead-footer">
      <div class="footer-col attorney">
        <span class="attorney-name">DANIEL R. HARTWELL, ESQ.</span><br>
        Licensed in NC and FL<br>
        Board Certified in Civil Trial Law<br>
        by NTCA
      </div>
      <div class="footer-col office">
        2480 Linden Avenue, Suite 410<br>
        Cary, NC 27511<br>
        <span class="label">T:</span> 919.555.0142<br>
        <span class="label">F:</span> 919.555.0163
      </div>
      <div class="footer-web">www.<strong>hartwelllawpa</strong>.com</div>
    </footer>
  </section>

  <section class="sheet business-card" aria-label="Business card">
    <div class="card-band top"></div>
    <div class="brand">
      <div class="brand-circle"></div>
      <div class="brand-name">HARTWELL LAW</div>
    </div>
    <div class="card-details identity">
      <div class="card-name">DANIEL R. HARTWELL, ESQ.</div>
      Licensed in NC and FL<br>
      Board Certified in Civil Trial Law
    </div>
    <div class="card-details contact">
      <span class="label">T:</span> 919.555.0142<br>
      <span class="label">C:</span> 919.555.0187<br>
      dan@hartwelllawpa.com<br>
      www.hartwelllawpa.com
    </div>
    <div class="card-details address">
      2480 Linden Avenue, Suite 410<br>
      Cary, NC 27511
    </div>
    <div class="card-band bottom"></div>
  </section>

  <section class="sheet envelope-back" aria-label="Envelope back">
    <svg class="envelope-flap" width="487" height="70" viewBox="0 0 487 70" aria-hidden="true">
      <path d="M0 0 H487 L480 50 Q477 69 458 69 H29 Q12 69 8 50 Z" fill="var(--navy)"/>
    </svg>
  </section>

  <section class="sheet envelope-front" aria-label="Envelope front">
    <div class="brand">
      <div class="brand-circle"></div>
      <div class="brand-name">HARTWELL LAW</div>
    </div>
    <div class="return-address">
      2480 Linden Avenue, Suite 410<br>
      Cary, NC 27511
    </div>
  </section>

</body>
</html>
```